Home brewer beer bottle label

I need a label for home-brew beer bottles. My sons and I all make our own beer. It should say Kessner Ale in blackletter (because we are of German heritage) (EDIT: ACTUALLY WE ARE LIKING OTHER TYPEFACE NOW) and the designer will need to work in aspects of the Kessner family (crest attached). Finally we will need two blank areas or lines for (1) what kind of beer (handwritten) and (2) who made it (the Beerista!) I have attached a rough sketch, but feel free to ignore and be creative. No color requirements. (EDIT: ACTUALLY, MY WIFE LIKES THE LITTLE BIT OF PURPLE IN THE 4TH DESIGN) Would like the logotype portion of the label to be usable on its own as a family logo. (EDIT; THIS IS LESS IMPORTANT NOW). I have attached another file sketch, which shows using the parts of the family crest w/out trying to replicate it. Thanks, everyone, for the good work....
Updates

Project Deadline Extended
Reason: Extending because my wife is out of town until Wednesday and I need her input.

Target Market(s)

Mostly friends and family at the wedding.

Industry/Entity Type

Work

Font styles to use
Serif
Sans Serif

Requirements
Must have
• Tightly kerned lettering,
Nice to have
• Color, one Group of Elements in Indesign and the print file, "Beer" and "Beerista" lines
Should not have
• Hard to see logo or logo type

```html
<!DOCTYPE html>
<html lang="en">
<head>
<meta charset="utf-8">
<title>Kessner Ale – Bottle Label Options</title>
<link href="https://fonts.googleapis.com/css2?family=UnifrakturMaguntia&family=PT+Sans&display=swap" rel="stylesheet">
<style>
  :root {
    --page: #ffffff;
    --ink: #111111;
    --gold-dark: #5e4d1d;
    --gold-mid: #a8954f;
    --gold-light: #efe9c8;
    --blue-light: #1cbdee;
    --blue-dark: #0a6db5;
    --ring-blue: #1f4fa8;
    --ring-gold: #dcb862;
    --sand: #dcc07a;
    --rule: #6d6d6d;
    --crest-blue: #3a55a8;
    --crest-yellow: #e4c43c;
    --gold: linear-gradient(90deg, #7d6a2c 0%, #c8b774 22%, #f3efd6 42%, #c9b874 60%, #8a7633 80%, #4f3f17 100%);
    --blue: linear-gradient(90deg, var(--blue-light) 0%, #1398d8 45%, var(--blue-dark) 100%);
  }
  * { box-sizing: border-box; margin: 0; padding: 0; }
  html, body { width: 734px; height: 1200px; overflow: hidden; background: var(--page); }
  .sheet { position: relative; width: 734px; height: 1200px; }
  .section-title {
    position: absolute; font-family: "PT Sans", Arial, sans-serif;
    font-size: 18px; color: var(--ink);
  }
  .finish-gold { background: var(--gold); }
  .finish-blue { background: var(--blue); }

  /* hang tags */
  .tag {
    position: absolute; top: 95px; width: 140px; height: 205px;
    border-radius: 34px 34px 26px 26px / 44px 44px 26px 26px;
  }
  .tag-hole {
    position: absolute; top: 7px; left: 64px; width: 11px; height: 11px;
    border-radius: 50%; background: #d9d9d9; border: 1px solid #888;
  }
  .emblem {
    position: absolute; border-radius: 50%;
    background: var(--ring-gold); padding: 4px;
  }
  .emblem-ring {
    width: 100%; height: 100%; border-radius: 50%;
    background: var(--ring-blue); padding: 6px;
  }
  .emblem-core {
    width: 100%; height: 100%; border-radius: 50%; background: #fff;
    display: flex; align-items: center; justify-content: center;
  }
  .crest {
    background: radial-gradient(ellipse at 50% 55%, var(--crest-blue) 0 30%, var(--crest-yellow) 55%, rgba(228,196,60,0.25) 75%, transparent 76%);
  }
  .brand {
    position: absolute; left: 0; width: 100%; text-align: center;
    font-family: "UnifrakturMaguntia", serif; color: var(--ink);
    letter-spacing: 0.5px; white-space: nowrap;
  }
  .tag .brand { top: 166px; font-size: 17px; }

  .tag-back-panel { position: absolute; left: 19px; top: 28px; }
  .tag-back-panel svg { display: block; }
  .field-label {
    font-family: "UnifrakturMaguntia", serif; font-size: 11px; fill: var(--ink);
  }

  /* flat labels */
  .label { position: absolute; width: 178px; height: 274px; }
  .label .brand { font-size: 17px; }
  .write-in {
    position: absolute; left: 8px; right: 8px; display: flex; align-items: flex-end;
    font-family: "UnifrakturMaguntia", serif; font-size: 11px; color: var(--ink);
  }
  .write-in .box {
    width: 8px; height: 8px; border: 1.5px solid #222; background: var(--sand);
    margin-right: 4px; margin-bottom: 2px; flex: none;
  }
  .write-in .line { flex: 1; border-bottom: 1px solid var(--rule); margin-left: 10px; margin-bottom: 3px; }
</style>
</head>
<body>
<main class="sheet">

  <h2 class="section-title" style="left:37px; top:46px;">Double sided:</h2>

  <!-- gold tag pair -->
  <div class="tag finish-gold" style="left:38px;">
    <span class="tag-hole"></span>
    <div class="emblem" style="left:5px; top:20px; width:130px; height:130px;">
      <div class="emblem-ring"><div class="emblem-core">
        <div class="crest" role="img" aria-label="Kessner family crest illustration" style="width:82px; height:82px;"></div>
      </div></div>
    </div>
    <div class="brand">Kessner Ale</div>
  </div>
  <div class="tag finish-gold" style="left:193px;">
    <span class="tag-hole"></span>
    <div class="tag-back-panel">
      <svg width="102" height="150" viewBox="0 0 102 150">
        <path d="M51 2 C86 2 100 28 100 60 L100 104 L51 148 L2 104 L2 60 C2 28 16 2 51 2 Z" fill="var(--sand)" stroke="#fff" stroke-width="2.5"/>
        <path d="M2 104 L100 104 L51 148 Z" fill="var(--ring-blue)"/>
        <text class="field-label" x="51" y="20" text-anchor="middle">Beer</text>
        <path d="M51 24 V32 M48 29 L51 33 L54 29" stroke="#111" stroke-width="1" fill="none"/>
        <line x1="20" y1="46" x2="82" y2="46" stroke="var(--rule)" stroke-width="0.8"/>
        <text class="field-label" x="51" y="62" text-anchor="middle">Beerista</text>
        <path d="M51 66 V74 M48 71 L51 75 L54 71" stroke="#111" stroke-width="1" fill="none"/>
        <line x1="20" y1="92" x2="82" y2="92" stroke="var(--rule)" stroke-width="0.8"/>
        <path d="M51 118 L40 112 L40 124 Z M51 118 L62 112 L62 124 Z M51 118 L45 130 M51 118 L57 130" stroke="#fff" stroke-width="1.5" fill="#fff"/>
      </svg>
    </div>
  </div>

  <!-- blue tag pair -->
  <div class="tag finish-blue" style="left:377px;">
    <span class="tag-hole"></span>
    <div class="emblem" style="left:5px; top:20px; width:130px; height:130px;">
      <div class="emblem-ring"><div class="emblem-core">
        <div class="crest" role="img" aria-label="Kessner family crest illustration" style="width:82px; height:82px;"></div>
      </div></div>
    </div>
    <div class="brand">Kessner Ale</div>
  </div>
  <div class="tag finish-blue" style="left:532px;">
    <span class="tag-hole"></span>
    <div class="tag-back-panel">
      <svg width="102" height="150" viewBox="0 0 102 150">
        <path d="M51 2 C86 2 100 28 100 60 L100 104 L51 148 L2 104 L2 60 C2 28 16 2 51 2 Z" fill="var(--sand)" stroke="#fff" stroke-width="2.5"/>
        <path d="M2 104 L100 104 L51 148 Z" fill="var(--ring-blue)"/>
        <text class="field-label" x="51" y="20" text-anchor="middle">Beer</text>
        <path d="M51 24 V32 M48 29 L51 33 L54 29" stroke="#111" stroke-width="1" fill="none"/>
        <line x1="20" y1="46" x2="82" y2="46" stroke="var(--rule)" stroke-width="0.8"/>
        <text class="field-label" x="51" y="62" text-anchor="middle">Beerista</text>
        <path d="M51 66 V74 M48 71 L51 75 L54 71" stroke="#111" stroke-width="1" fill="none"/>
        <line x1="20" y1="92" x2="82" y2="92" stroke="var(--rule)" stroke-width="0.8"/>
        <path d="M51 118 L40 112 L40 124 Z M51 118 L62 112 L62 124 Z M51 118 L45 130 M51 118 L57 130" stroke="#fff" stroke-width="1.5" fill="#fff"/>
      </svg>
    </div>
  </div>

  <h2 class="section-title" style="left:47px; top:396px;">One sided:</h2>

  <!-- row one -->
  <div class="label finish-gold" style="left:47px; top:447px;">
    <div class="emblem" style="left:19px; top:28px; width:140px; height:140px;">
      <div class="emblem-ring"><div class="emblem-core">
        <div class="crest" role="img" aria-label="Kessner family crest illustration" style="width:90px; height:90px;"></div>
      </div></div>
    </div>
    <div class="brand" style="top:164px;">Kessner Ale</div>
    <div class="write-in" style="top:202px;"><span class="box"></span>Beer<span class="line"></span></div>
    <div class="write-in" style="top:243px;"><span class="box"></span>Beerista<span class="line"></span></div>
  </div>

  <div class="label finish-blue" style="left:269px; top:447px;">
    <div class="emblem" style="left:19px; top:28px; width:140px; height:140px;">
      <div class="emblem-ring"><div class="emblem-core">
        <div class="crest" role="img" aria-label="Kessner family crest illustration" style="width:90px; height:90px;"></div>
      </div></div>
    </div>
    <div class="brand" style="top:164px;">Kessner Ale</div>
    <div class="write-in" style="top:202px;"><span class="box"></span>Beer<span class="line"></span></div>
    <div class="write-in" style="top:243px;"><span class="box"></span>Beerista<span class="line"></span></div>
  </div>

  <div class="label finish-gold" style="left:508px; top:447px;">
    <div class="crest" role="img" aria-label="Kessner family crest with name banner" style="position:absolute; left:34px; top:42px; width:110px; height:110px;"></div>
    <div class="brand" style="top:160px;">Kessner Ale</div>
    <div class="write-in" style="top:202px;"><span class="box"></span>Beer<span class="line"></span></div>
    <div class="write-in" style="top:243px;"><span class="box"></span>Beerista<span class="line"></span></div>
  </div>

  <!-- row two -->
  <div class="label finish-blue" style="left:45px; top:806px;">
    <div class="crest" role="img" aria-label="Kessner family crest with name banner" style="position:absolute; left:29px; top:10px; width:120px; height:140px;"></div>
    <div class="brand" style="top:155px;">Kessner Ale</div>
    <div class="write-in" style="top:203px;"><span class="box"></span>Beer<span class="line"></span></div>
    <div class="write-in" style="top:244px;"><span class="box"></span>Beerista<span class="line"></span></div>
  </div>

  <div class="label finish-gold" style="left:271px; top:806px;">
    <div class="crest" role="img" aria-label="Kessner family crest with name banner" style="position:absolute; left:29px; top:10px; width:120px; height:140px;"></div>
    <div class="brand" style="top:155px;">Kessner Ale</div>
    <div class="write-in" style="top:203px;"><span class="box"></span>Beer<span class="line"></span></div>
    <div class="write-in" style="top:244px;"><span class="box"></span>Beerista<span class="line"></span></div>
  </div>

  <div class="label finish-gold" style="left:508px; top:806px;">
    <div class="brand" style="top:16px; font-size:23px;">Kessner Ale</div>
    <div class="crest" role="img" aria-label="Kessner family crest with name banner" style="position:absolute; left:34px; top:52px; width:110px; height:130px;"></div>
    <div class="write-in" style="top:203px;"><span class="box"></span>Beer<span class="line"></span></div>
    <div class="write-in" style="top:244px;"><span class="box"></span>Beerista<span class="line"></span></div>
  </div>

</main>
</body>
</html>
```